We need a small, simple graphic for the company newsletter. The topic of this issue is voting. As a company, we believe it is important to vote; therefore, we're going to explain the importance of voting, how to vote, when to vote, and how the company will be providing time off to vote. We would like the graphic to be simple (2-3 colors) and look like the sticker or pin you received after voting that says "I voted". We would like our company logo incorporated somehow, so be creative. It must contain our company color of blue (r 38, g 58, b 128). The company logo is attached, as well as some I voted stickers for reference

Requirements
Must have
• Use our company color of blue (r 38 g 58 b 128). Use the words "I Voted". Use the company font Bebas and/or Helvetica Neue. The background must be white as it will be incorporated into a newsletter document.
Nice to have
• Incorporate the company logo. American flag
Should not have
• fireworks, reference to 2020

```html
<!DOCTYPE html>
<html lang="en">
<head>
<meta charset="utf-8">
<title>I Voted Sticker</title>
<link rel="stylesheet" href="https://fonts.googleapis.com/css2?family=Bebas+Neue&display=swap">
<style>
  :root {
    --brand-blue: #263a80;
    --field-blue: #33506f;
    --stripe-red: #c4474e;
    --stripe-white: #f6f5f3;
    --star-white: #f1f1ef;
    --page-white: #ffffff;
    --sticker-white: #f4f4f4;
  }
  html, body {
    margin: 0;
    padding: 0;
    width: 1200px;
    height: 900px;
    overflow: hidden;
    background: var(--page-white);
  }
  .sticker {
    display: block;
    width: 1200px;
    height: 900px;
  }
  .sticker-base { fill: var(--sticker-white); }
  .flag-field { fill: var(--field-blue); }
  .flag-star { fill: var(--star-white); }
  .stripe-red { fill: var(--stripe-red); }
  .stripe-white { fill: var(--stripe-white); }
  .voted-label {
    font-family: "Bebas Neue", "Helvetica Neue", Arial, sans-serif;
    font-size: 150px;
    fill: var(--brand-blue);
    letter-spacing: 2px;
  }
  .company-name {
    font-family: "Bebas Neue", "Helvetica Neue", Arial, sans-serif;
    font-size: 46px;
    fill: var(--brand-blue);
    letter-spacing: 2px;
  }
</style>
</head>
<body>
<svg class="sticker" viewBox="0 0 1200 900" xmlns="http://www.w3.org/2000/svg" role="img" aria-label="Round I Voted sticker with flag stripes and stars">
  <defs>
    <clipPath id="sticker-shape">
      <circle cx="600" cy="450" r="250"/>
    </clipPath>
    <linearGradient id="stripe-fade" x1="0" y1="0" x2="0" y2="1" gradientUnits="objectBoundingBox">
      <stop offset="0" stop-color="#fff" stop-opacity="1"/>
      <stop offset="0.45" stop-color="#fff" stop-opacity="0.95"/>
      <stop offset="0.8" stop-color="#fff" stop-opacity="0"/>
    </linearGradient>
    <mask id="stripe-mask" maskUnits="userSpaceOnUse" x="200" y="320" width="800" height="420">
      <rect x="200" y="320" width="800" height="420" fill="url(#stripe-fade)"/>
    </mask>
  </defs>

  <g clip-path="url(#sticker-shape)">
    <rect class="sticker-base" x="340" y="190" width="520" height="520"/>

    <g transform="rotate(-12 600 450)">
      <g class="flag-stripes" mask="url(#stripe-mask)">
        <rect class="stripe-white" x="250" y="320" width="700" height="420"/>
        <rect class="stripe-red" x="250" y="320" width="55" height="420"/>
        <rect class="stripe-red" x="360" y="320" width="55" height="420"/>
        <rect class="stripe-red" x="470" y="320" width="55" height="420"/>
        <rect class="stripe-red" x="580" y="320" width="55" height="420"/>
        <rect class="stripe-red" x="690" y="320" width="55" height="420"/>
        <rect class="stripe-red" x="800" y="320" width="55" height="420"/>
      </g>

      <rect class="flag-field" x="250" y="120" width="700" height="205"/>

      <g class="flag-stars">
        <polygon class="flag-star" points="0,-20 5.9,-6.2 19,-6.2 8.5,2.4 12.3,16.2 0,8 -12.3,16.2 -8.5,2.4 -19,-6.2 -5.9,-6.2" transform="translate(430 285)"/>
        <polygon class="flag-star" points="0,-20 5.9,-6.2 19,-6.2 8.5,2.4 12.3,16.2 0,8 -12.3,16.2 -8.5,2.4 -19,-6.2 -5.9,-6.2" transform="translate(470 235)"/>
        <polygon class="flag-star" points="0,-20 5.9,-6.2 19,-6.2 8.5,2.4 12.3,16.2 0,8 -12.3,16.2 -8.5,2.4 -19,-6.2 -5.9,-6.2" transform="translate(525 285)"/>
        <polygon class="flag-star" points="0,-20 5.9,-6.2 19,-6.2 8.5,2.4 12.3,16.2 0,8 -12.3,16.2 -8.5,2.4 -19,-6.2 -5.9,-6.2" transform="translate(560 230)"/>
        <polygon class="flag-star" points="0,-20 5.9,-6.2 19,-6.2 8.5,2.4 12.3,16.2 0,8 -12.3,16.2 -8.5,2.4 -19,-6.2 -5.9,-6.2" transform="translate(615 285)"/>
        <polygon class="flag-star" points="0,-20 5.9,-6.2 19,-6.2 8.5,2.4 12.3,16.2 0,8 -12.3,16.2 -8.5,2.4 -19,-6.2 -5.9,-6.2" transform="translate(655 225)"/>
        <polygon class="flag-star" points="0,-20 5.9,-6.2 19,-6.2 8.5,2.4 12.3,16.2 0,8 -12.3,16.2 -8.5,2.4 -19,-6.2 -5.9,-6.2" transform="translate(705 280)"/>
        <polygon class="flag-star" points="0,-20 5.9,-6.2 19,-6.2 8.5,2.4 12.3,16.2 0,8 -12.3,16.2 -8.5,2.4 -19,-6.2 -5.9,-6.2" transform="translate(745 225)"/>
        <polygon class="flag-star" points="0,-20 5.9,-6.2 19,-6.2 8.5,2.4 12.3,16.2 0,8 -12.3,16.2 -8.5,2.4 -19,-6.2 -5.9,-6.2" transform="translate(795 280)"/>
      </g>

      <text class="voted-label" x="590" y="535" text-anchor="middle">I VOTED</text>
    </g>

    <text class="company-name" x="640" y="615" text-anchor="middle">KESTREL ROW</text>
  </g>
</svg>
</body>
</html>
```